Themed design for packaging sleeve and box

1) Gable box 330w x 200d x 160h (image attached for illustration purposes)
2) Sleeve to wrap around our food trays - see image attached

See the images uploaded!!!
This should not be copied, as some are from our competitors and are subject to Copywrite but gives an idea what kind of packaging we would be creating

From all the designs submitted, we will choose one final design and work with this designer to create our full packaging range.....

Target Market(s)

Working adults and health mined people

Font styles to use
Sans Serif

Colors

Designer to choose colors to be used in the design.

Requirements
Must have
• A clean modern look, striking design
Same design in different colours (see the drink bottles idea)
1) meat in shades of red
2) fish in shades of blue
3) vegetable in shades of green
Nice to have
• abstract white against strong colours
use shapes or mosaic or shades of the same colours
Should not have
• overpacked designs with too much information

```html
<!DOCTYPE html>
<html lang="en">
<head>
<meta charset="utf-8">
<title>Evenfare – Tray Sleeve, Option 1</title>
<link rel="stylesheet" href="https://fonts.googleapis.com/css2?family=Arimo&family=Oswald:wght@500&display=swap">
<style>
  :root {
    --ink: #000000;
    --paper: #ffffff;
    --fish-blue: #0b4c9b;
    --meat-red: #e3131f;
    --veg-green: #0c8c3a;
    --brand-lime: #8cc63f;
    --fold: #3a3a3a;
    --body-font: "Arimo", Arial, sans-serif;
    --label-font: "Oswald", "Arial Narrow", sans-serif;
  }
  * { margin: 0; padding: 0; box-sizing: border-box; }
  html, body { width: 1200px; height: 1033px; overflow: hidden; background: var(--paper); }
  .sheet { position: relative; width: 1200px; height: 1033px; font-family: var(--body-font); color: var(--ink); }

  .sheet-title { position: absolute; left: 158px; top: 96px; font-size: 48px; font-weight: 400; letter-spacing: 0.5px; }

  .dimensions { position: absolute; left: 0; top: 0; width: 1200px; height: 480px; }
  .dim-label { position: absolute; font-size: 19px; transform: translate(-50%, -50%); }

  .dieline { position: absolute; left: 159px; top: 263px; width: 895px; height: 191px; border: 1px solid var(--ink); background: var(--paper); overflow: hidden; }
  .panel { position: absolute; top: 0; height: 100%; }
  .panel--colour { background: var(--fish-blue); }
  .fold-line { position: absolute; top: 0; height: 100%; border-left: 1px dashed var(--fold); }
  .panel--colour .fold-line, .fold-line--on-colour { border-left-color: #05244d; }

  .dish-name { position: absolute; font-family: var(--label-font); font-weight: 500; color: var(--paper); text-align: right; text-transform: uppercase; line-height: 1.15; }
  .brand-name { position: absolute; font-family: var(--label-font); font-weight: 500; color: var(--brand-lime); letter-spacing: 2px; text-transform: uppercase; white-space: nowrap; line-height: 1; }
  .brand-name--white { color: var(--paper); }
  .brand-name--vertical-up { transform: translate(-50%, -50%) rotate(-90deg); }
  .brand-name--vertical-down { transform: translate(-50%, -50%) rotate(90deg); }
  .ingredients { position: absolute; font-size: 8px; color: var(--ink); white-space: nowrap; }

  .sleeve { position: absolute; width: 260px; height: 136px; background: linear-gradient(135deg, #ffffff 55%, #e9e9e9 100%); border: 1px solid #d0d0d0; }
  .sleeve .colour-block { position: absolute; left: 0; top: 0; width: 100px; height: 100%; }
  .sleeve--fish .colour-block { background: var(--fish-blue); }
  .sleeve--meat .colour-block { background: var(--meat-red); }
  .sleeve--veg .colour-block { background: var(--veg-green); }
  .sleeve .dish-name { right: 168px; bottom: 4px; font-size: 11px; }
  .sleeve .brand-name { left: 121px; top: 14px; font-size: 19px; }
  .sleeve .ingredients { left: 109px; top: 104px; font-size: 5px; }
</style>
</head>
<body>
<main class="sheet">
  <h1 class="sheet-title">OPTION 1</h1>

  <svg class="dimensions" viewBox="0 0 1200 480" aria-hidden="true">
    <g stroke="#000" stroke-width="1" fill="none">
      <line x1="159" y1="173" x2="159" y2="207"/>
      <line x1="1054" y1="173" x2="1054" y2="207"/>
      <line x1="162" y1="189" x2="1051" y2="189"/>
      <line x1="159" y1="229" x2="1054" y2="229"/>
      <line x1="159" y1="213" x2="159" y2="246"/>
      <line x1="316" y1="213" x2="316" y2="246"/>
      <line x1="440" y1="213" x2="440" y2="246"/>
      <line x1="795" y1="213" x2="795" y2="246"/>
      <line x1="919" y1="213" x2="919" y2="246"/>
      <line x1="1054" y1="213" x2="1054" y2="246"/>
      <line x1="108" y1="263" x2="142" y2="263"/>
      <line x1="108" y1="454" x2="142" y2="454"/>
      <line x1="125" y1="266" x2="125" y2="451"/>
    </g>
    <g fill="#000">
      <polygon points="160,189 172,183 169,189 172,195"/>
      <polygon points="1053,189 1041,183 1044,189 1041,195"/>
      <polygon points="125,264 119,276 125,273 131,276"/>
      <polygon points="125,453 119,441 125,444 131,441"/>
    </g>
  </svg>
  <span class="dim-label" style="left:607px; top:164px;">398</span>
  <span class="dim-label" style="left:224px; top:213px;">70</span>
  <span class="dim-label" style="left:376px; top:213px;">55</span>
  <span class="dim-label" style="left:614px; top:213px;">158</span>
  <span class="dim-label" style="left:855px; top:213px;">55</span>
  <span class="dim-label" style="left:985px; top:213px;">60</span>
  <span class="dim-label" style="left:95px; top:357px;">85</span>

  <section class="dieline" aria-label="Sleeve dieline, fish range">
    <div class="panel panel--colour" style="left:157px; width:258px;">
      <span class="fold-line" style="left:118px;"></span>
      <span class="fold-line" style="left:131px;"></span>
    </div>
    <div class="panel panel--colour" style="left:636px; width:124px;"></div>
    <span class="fold-line" style="left:630px;"></span>
    <span class="fold-line fold-line--on-colour" style="left:643px;"></span>

    <span class="brand-name brand-name--white brand-name--vertical-down" style="left:228px; top:97px; font-size:20px;">Evenfare</span>
    <p class="dish-name" style="right:480px; top:147px; font-size:17px;">Thai Green<br>Chicken Curry</p>
    <span class="brand-name" style="left:445px; top:20px; font-size:28px;">Evenfare</span>
    <span class="ingredients" style="left:428px; top:150px;">Ingredients text etc</span>
    <span class="brand-name brand-name--white brand-name--vertical-up" style="left:691px; top:97px; font-size:20px;">Evenfare</span>
    <span class="brand-name brand-name--vertical-up" style="left:779px; top:76px; font-size:20px;">Evenfare</span>
  </section>

  <article class="sleeve sleeve--fish" style="left:149px; top:622px;" aria-label="Sleeve front, fish range">
    <div class="colour-block"></div>
    <span class="brand-name">Evenfare</span>
    <p class="dish-name">Thai Green<br>Chicken Curry</p>
    <span class="ingredients">Ingredients text etc</span>
  </article>

  <article class="sleeve sleeve--meat" style="left:473px; top:629px;" aria-label="Sleeve front, meat range">
    <div class="colour-block"></div>
    <span class="brand-name">Evenfare</span>
    <p class="dish-name">Thai Green<br>Chicken Curry</p>
    <span class="ingredients">Ingredients text etc</span>
  </article>

  <article class="sleeve sleeve--veg" style="left:819px; top:622px;" aria-label="Sleeve front, vegetable range">
    <div class="colour-block"></div>
    <span class="brand-name">Evenfare</span>
    <p class="dish-name">Thai Green<br>Chicken Curry</p>
    <span class="ingredients">Ingredients text etc</span>
  </article>
</main>
</body>
</html>
```